Design the app for the next Dwelvo

We need a cutting edge, super UX-intuitive, design for a global parking app called Sloto.
- Homescreen and website have been finalised already (see attached pdf)
- Wireframed screens for the concepts we need have been provided in the attached pdf
- We need some really nice icons for parking space types, etc
- Needs to be very, very intuitive to use and navigate.
References: Dwelvo app & Zipto app, for their simplicity of use
Reason: A few designers have requested that we extend this deadline. So here you go.
Parking

```html
<!DOCTYPE html>
<html lang="en">
<head>
<meta charset="utf-8">
<title>Sloto – Parking Space</title>
<link href="https://fonts.googleapis.com/css2?family=Open+Sans:wght@300;400;600&display=swap" rel="stylesheet">
<style>
:root{
  --stage:#36444d;
  --ink:#2b2b2b;
  --muted:#555;
  --rule:#e6e6e6;
  --panel:#f6f6f6;
  --accent-yellow:#f6e34b;
  --score-green:#8dc63f;
  --book-red:#e8392e;
  --price-blue:#1f7fc4;
  --hero-band:rgba(38,52,66,.82);
}
*{box-sizing:border-box;margin:0;padding:0}
html,body{width:1200px;height:1200px;overflow:hidden;background:var(--stage);font-family:"Open Sans",sans-serif;color:var(--ink)}
.screen{position:absolute;left:400px;top:14px;width:427px;height:1250px;background:#fff;transform:scale(.94);transform-origin:top left;overflow:hidden}
.hero{position:relative;height:327px;color:#fff}
.hero-photo{position:absolute;inset:0;background:linear-gradient(120deg,#a88a5c 0%,#c2a676 25%,#2f86c9 45%,#1e6fb0 70%,#8c7450 100%)}
.status{position:absolute;top:4px;left:8px;right:8px;display:flex;justify-content:space-between;font-size:14px}
.status .battery{display:inline-block;width:28px;height:11px;border:1px solid #fff;margin-left:4px;vertical-align:-1px;position:relative}
.status .battery::before{content:"";position:absolute;left:1px;top:1px;bottom:1px;width:6px;background:#fff}
.header{position:absolute;top:34px;left:24px;right:24px;display:flex;align-items:flex-start}
.back{margin-top:12px;margin-right:20px}
.title{font-size:18px;font-weight:400;line-height:24px}
.stars{color:#f6d21a;font-size:11px;letter-spacing:1px}
.heart{margin-left:auto;margin-top:8px}
.hero-band{position:absolute;left:0;right:0;bottom:0;height:79px;background:var(--hero-band);display:flex;padding:18px 26px 0 27px}
.score{font-size:22px;color:var(--score-green);line-height:26px}
.score small{display:block;font-size:12px;color:#fff;line-height:16px}
.address{margin-left:auto;display:flex;gap:10px;font-size:15px;line-height:20px}
.tabs{display:flex;height:63px;border-bottom:1px solid var(--rule);background:#fafafa;font-size:13px;font-weight:600;color:#444}
.tab{flex:1;display:flex;align-items:center;justify-content:center;position:relative}
.tab.active::after{content:"";position:absolute;left:0;right:0;bottom:-1px;height:3px;background:var(--accent-yellow)}
.section{text-align:center;border-bottom:1px solid var(--rule)}
.section h2{font-weight:400;font-size:19px;letter-spacing:.3px}
.ideal{height:86px;padding-top:20px}
.ideal p{font-size:15px;color:var(--muted);margin-top:6px;font-weight:300}
.description{height:261px;padding:16px 18px 0}
.description p{font-size:15.5px;line-height:22px;color:var(--muted);font-weight:300;margin-top:8px}
.description p+p{margin-top:22px}
.features-head{height:55px;padding-top:14px}
.features{height:94px;background:var(--panel);display:flex;padding:18px 0 0 4px;border-bottom:1px solid var(--rule)}
.feature{width:85px;text-align:center;font-size:9px;color:#444}
.feature svg{display:block;margin:0 auto 8px}
.map-head{height:61px;padding-top:20px;border-bottom:none}
.map{height:229px;background:linear-gradient(135deg,#e8e4dc,#d6d2c8 60%,#e4e1d8)}
.footer{display:flex;height:74px}
.price{flex:1;background:var(--panel);text-align:center;padding-top:14px}
.price strong{display:block;font-weight:400;font-size:23px;color:var(--price-blue);line-height:26px}
.price span{font-size:12px}
.book{flex:1;background:var(--book-red);color:#fff;display:flex;align-items:center;justify-content:center;gap:12px;font-size:16px;letter-spacing:.5px}
</style>
</head>
<body>
<main class="screen">
  <header class="hero">
    <div class="hero-photo" role="img" aria-label="Photo of a blue scooter parked against a weathered stone wall"></div>
    <div class="status"><span>●●●●○ VOLT</span><span>4:21 PM</span><span>22%<i class="battery"></i></span></div>
    <div class="header">
      <svg class="back" width="10" height="18" viewBox="0 0 10 18"><path d="M9 1 1 9l8 8" fill="none" stroke="#fff" stroke-width="1.5"/></svg>
      <div><div class="title">Parking Space</div><div class="stars">★★★★★</div></div>
      <svg class="heart" width="20" height="18" viewBox="0 0 20 18"><path d="M10 17 2 9A5 5 0 0 1 10 3a5 5 0 0 1 8 6z" fill="#fff"/></svg>
    </div>
    <div class="hero-band">
      <div class="score">85 / 100<small>Love this</small></div>
      <div class="address">
        <svg width="12" height="17" viewBox="0 0 12 17"><path d="M6 0a6 6 0 0 1 6 6c0 4-6 11-6 11S0 10 0 6a6 6 0 0 1 6-6z" fill="#fff"/><circle cx="6" cy="6" r="2.2" fill="#2a3a48"/></svg>
        <div>2310 Fenwick Street,<br>Harbor City, California</div>
      </div>
    </div>
  </header>

  <nav class="tabs">
    <div class="tab active">REVIEW</div>
    <div class="tab">AVAILABILITY</div>
    <div class="tab">MESSAGE</div>
  </nav>

  <section class="section ideal">
    <h2>IDEAL FOR</h2>
    <p>Members of Linden Golf Club</p>
  </section>

  <section class="section description">
    <h2>DESCRIPTION</h2>
    <p>Looking for somewhere to park in Linden and want to avoid the hassle of expensive council parking fees? This is the ideal spot for you. Quiet cul-de-sac with very little traffic. Right opposite the Linden Roundhouse childcare centre, and a stone’s throw from Linden Golf Club.</p>
    <p>Please park on the grass beside the concrete driveway.</p>
  </section>

  <section class="section features-head"><h2>FEATURES</h2></section>
  <div class="features">
    <div class="feature"><svg width="20" height="22" viewBox="0 0 20 22" fill="none" stroke="#333" stroke-width="1.6"><path d="M5 10V6a5 5 0 0 1 10 0v4"/><rect x="2" y="10" width="16" height="11"/><path d="M10 14v3"/></svg>SECURE</div>
    <div class="feature"><svg width="26" height="20" viewBox="0 0 26 20" fill="none" stroke="#333" stroke-width="1.6"><rect x="1" y="3" width="24" height="12"/><path d="M1 7h24M5 10h16M5 13h16"/></svg>COVERED</div>
    <div class="feature"><svg width="20" height="22" viewBox="0 0 20 22" fill="none" stroke="#333" stroke-width="1.6"><path d="M10 1 2 4v6c0 6 4 9 8 11 4-2 8-5 8-11V4z"/><path d="M6 10l3 3 5-6"/></svg>GUARDED</div>
    <div class="feature"><svg width="20" height="22" viewBox="0 0 20 22" fill="none" stroke="#333" stroke-width="1.6"><rect x="2" y="1" width="16" height="17" rx="3"/><path d="M2 10h16M5 21v-3M15 21v-3"/><circle cx="6" cy="14" r="1"/><circle cx="14" cy="14" r="1"/></svg>LARGE</div>
  </div>

  <section class="section map-head"><h2>MAP</h2></section>
  <div class="map" role="img" aria-label="Street map showing the parking space location"></div>

  <footer class="footer">
    <div class="price"><strong>$ 10</strong><span>PER DAY</span></div>
    <div class="book">
      <svg width="18" height="20" viewBox="0 0 18 20" fill="none" stroke="#fff" stroke-width="1.5"><path d="M2 6h14l-1 13H3z"/><path d="M6 8V4a3 3 0 0 1 6 0v4"/></svg>
      BOOK NOW
    </div>
  </footer>
</main>
</body>
</html>
```